Private Optometric Practice Needs new Presentation Folders/Stationary

We recently moved our office and are looking to refresh our presentation folders and stationary. I tend to prefer simple, clean designs. We are a full scope optometric practice provide high quality eyewear, custom contact lenses, along with emergency care and treatment for dry eyes. We communicate with a lot of other doctors and want to exude professionalism. I have attached 2 versions of our logo.

Target Market(s)

Familys

Industry/Entity Type

Eyecare

Font styles to use
Sans Serif

Colors
0054AA
0677BA
7BADD7
CADEEF
E8F1F8

Requirements
Nice to have
• Bifold, areas to put information about practice, welcome letter

```html
<!DOCTYPE html>
<html lang="en">
<head>
<meta charset="utf-8">
<title>Northfield Vision — Stationery Set</title>
<link rel="stylesheet" href="https://fonts.googleapis.com/css2?family=Poppins:wght@400;500;600;700&display=swap">
<style>
  :root{
    --blue:#38a9e0;
    --blue-deep:#0677ba;
    --ink:#1c1c1c;
    --text:#333333;
    --brand-grey:#5a5a5a;
    --paper:#ffffff;
    --bg-top:#f7f7f8;
    --bg-bottom:#e8e8ea;
    --faint:#f1f1f3;
    --window:#d4d4d6;
  }
  *{box-sizing:border-box;margin:0;padding:0}
  html,body{width:1200px;height:721px;overflow:hidden}
  body{
    font-family:"Poppins",sans-serif;
    background:linear-gradient(180deg,var(--bg-top) 0%,var(--bg-bottom) 100%);
    position:relative;color:var(--text);
  }
  .sheet{position:absolute;background:var(--paper);box-shadow:0 1px 4px rgba(0,0,0,.08);overflow:hidden}

  /* brand lockup */
  .brand{display:flex;flex-direction:column;align-items:center;position:absolute;left:50%;transform:translateX(-50%)}
  .brand-dot{border-radius:50%;background:var(--blue)}
  .brand-name{font-family:"Poppins",sans-serif;font-weight:400;color:var(--brand-grey);text-align:center;text-transform:uppercase;white-space:nowrap}

  /* envelope */
  .envelope{left:78px;top:141px;width:357px;height:155px}
  .envelope .brand{top:7px}
  .envelope .brand-dot{width:11px;height:11px;margin-bottom:3px}
  .envelope .brand-name{font-size:5.6px;letter-spacing:1.6px;line-height:6.6px}
  .envelope-accent{position:absolute;left:210px;top:-12px;width:190px;height:190px;border-radius:50%;background:var(--faint)}
  .envelope-window{position:absolute;left:21px;top:80px;width:100px;height:57px;border-radius:5px;
    background:linear-gradient(120deg,#d9d9db 0%,#ececed 40%,#d2d2d4 55%,#e3e3e5 100%);
    border:1px solid #c9c9cb;font-size:5.2px;color:#777}
  .envelope-window .to{position:absolute;left:11px;top:19px}
  .envelope-window .to b{font-weight:600;color:#666}
  .envelope-window .addr{position:absolute;left:21px;top:27px}

  /* business cards */
  .card{top:326px;width:132px;height:75px}
  .card-front{left:139px}
  .card-front .brand{top:17px}
  .card-front .brand-dot{width:16px;height:16px;margin-bottom:5px}
  .card-front .brand-name{font-size:8.4px;letter-spacing:2.6px;line-height:9.4px}
  .card-back{left:303px}
  .card-back .mark{position:absolute;right:10px;top:9px;width:11px;height:11px;border-radius:50%;background:var(--blue)}
  .card-back .holder{position:absolute;left:9px;top:35px;font-size:5.3px;font-weight:500;color:var(--blue);letter-spacing:.1px}
  .contact{position:absolute;left:9px;top:46px;list-style:none;font-size:2.7px;line-height:3.4px;color:#444;text-transform:uppercase}
  .contact li{display:flex;gap:2px;align-items:flex-start;margin-bottom:.6px}
  .contact svg{width:3px;height:3px;flex:none;margin-top:.2px}

  /* letterhead */
  .letterhead{left:467px;top:141px;width:311px;height:439px}
  .letterhead .brand{top:15px}
  .letterhead .brand-dot{width:16px;height:16px;margin-bottom:6px}
  .letterhead .brand-name{font-size:8.4px;letter-spacing:2.6px;line-height:9.4px}
  .letter-accent{position:absolute;left:80px;top:168px;width:150px;height:150px;border-radius:50%;background:var(--faint)}
  .letter-body{position:absolute;left:32px;right:32px;top:0;font-size:5.2px;line-height:8.85px;color:var(--text)}
  .recipient{position:absolute;top:89px;left:2px;font-size:5.6px;line-height:8.6px}
  .recipient b{font-weight:500;color:var(--ink)}
  .recipient span{display:block;padding-left:10px;font-size:5.2px}
  .date{position:absolute;top:90px;right:0;font-size:5.6px;font-weight:500;color:var(--ink)}
  .meta{position:absolute;top:136px;left:0}
  .copy{position:absolute;top:172px;left:0;right:0;text-align:justify}
  .copy p{margin-bottom:8.8px}
  .signoff{position:absolute;top:331px;left:0}
  .signature{position:absolute;top:364px;left:0;font-weight:500;color:var(--ink)}
  .letter-footer{position:absolute;left:0;right:0;bottom:0;height:20px;background:var(--blue);
    display:flex;align-items:center;justify-content:center;gap:3px;font-size:3.4px;color:#fff;text-transform:uppercase}
  .letter-footer svg{width:3.6px;height:3.6px}

  /* folder */
  .folder{left:811px;top:141px;width:311px;height:439px}
  .folder .brand{top:15px}
  .folder .brand-dot{width:16px;height:16px;margin-bottom:6px}
  .folder .brand-name{font-size:8.4px;letter-spacing:2.6px;line-height:9.4px}
  .folder-title{position:absolute;left:0;right:0;top:153px;text-align:center;font-weight:700;font-size:15.6px;line-height:16px;color:var(--ink);text-transform:uppercase}
  .folder-desc{position:absolute;left:0;right:0;top:188px;text-align:center;font-size:7.4px;color:var(--ink)}
  .folder-accent{position:absolute;left:48px;top:262px;width:360px;height:360px;border-radius:50%;background:var(--blue)}
</style>
</head>
<body>

  <section class="sheet envelope" aria-label="Envelope">
    <div class="envelope-accent"></div>
    <div class="brand"><span class="brand-dot"></span><span class="brand-name">Northfield<br>Vision</span></div>
    <div class="envelope-window">
      <div class="to"><b>To : Ms.</b> Partner</div>
      <div class="addr">123 Sample Address Here</div>
    </div>
  </section>

  <section class="sheet card card-front" aria-label="Business card front">
    <div class="brand"><span class="brand-dot"></span><span class="brand-name">Northfield<br>Vision</span></div>
  </section>

  <section class="sheet card card-back" aria-label="Business card back">
    <span class="mark"></span>
    <div class="holder">DANIEL WHITMORE, O.D.</div>
    <ul class="contact">
      <li><svg viewBox="0 0 10 10"><path d="M5 0a3.6 3.6 0 0 0-3.6 3.6C1.4 6.3 5 10 5 10s3.6-3.7 3.6-6.4A3.6 3.6 0 0 0 5 0z" fill="#38a9e0"/></svg><span>1420 Maple Grove Ave.<br>Suite B<br>Lakeport, MI 48001</span></li>
      <li><svg viewBox="0 0 10 10"><path d="M2 0.5l2 2-1 1.3a6 6 0 0 0 3.2 3.2l1.3-1 2 2L8 9.5C4 9.5.5 6 .5 2z" fill="#38a9e0"/></svg><span>555-014-2280</span></li>
      <li><svg viewBox="0 0 10 10"><circle cx="5" cy="5" r="4.5" fill="#38a9e0"/></svg><span>www.northfieldvision.com</span></li>
    </ul>
  </section>

  <section class="sheet letterhead" aria-label="Letterhead">
    <div class="letter-accent"></div>
    <div class="brand"><span class="brand-dot"></span><span class="brand-name">Northfield<br>Vision</span></div>
    <div class="letter-body">
      <div class="recipient"><b>To : Ms. Partner</b><span>123 Sample Address Here, City</span></div>
      <div class="date">Date : January 04, 2021</div>
      <div class="meta">Sample Document Subject<br>Department Sample</div>
      <div class="copy">
        <p>Here is the subject of the letter</p>
        <p>Dear Ms. Partner,</p>
        <p>This is dummy text. It is only used to illustrate the gray value of the type. But is that really the case? Isn't it the same if I write "this is dummy text" or "Guaredisch nedunfeg"? Fegüned – not at all.</p>
        <p>Dummy text provides important information, like the legibility of the body text, the impression it makes on the reader, the harmony between the individual figures, how narrow or wide they appear. Dummy text should contain as many different letters as possible and should be written in the original language. It doesn't have to make sense, it just needs to be readable. Texts in foreign languages, like "Lorem ipsum", don't actually serve this purpose, as they provide a false impression of what the body text actually looks like. This is dummy text. It is only used to illustrate the gray value of the type. But is that really the case? Isn't it the same if I write "this is dummy text" or "Guaredisch nedunfeg"? Fegüned – not at all.</p>
      </div>
      <div class="signoff">Yours sincerely,<br>SAMPLE AG</div>
      <div class="signature">Northfield Vision</div>
    </div>
    <footer class="letter-footer">
      <svg viewBox="0 0 10 10"><circle cx="5" cy="5" r="4.5" fill="#fff"/></svg>
      <span>www.northfieldvision.com</span>
    </footer>
  </section>

  <section class="sheet folder" aria-label="Presentation folder cover">
    <div class="brand"><span class="brand-dot"></span><span class="brand-name">Northfield<br>Vision</span></div>
    <h1 class="folder-title">Your Document<br>Title Here</h1>
    <p class="folder-desc">Description here</p>
    <div class="folder-accent"></div>
  </section>

</body>
</html>
```